Frostvale Cold Packs needs stationery designed for their new logo

We have a new logo so now want all our stationery to be redesigned.
Frostvale is a gel ice pack product used by the seafood & food industry to transport chilled products around the world.

We would like to use our new logo with icy or snow backgrounds or elements.
Our company tag line is "Keep your products chilled for longer"
I'll attach our old business cards so that you can use the text off them.
2nd attachment is our new logo to be used.

We want a design for:
- Business cards
- Letter Head
- Email signature

Target Market(s)

seafood & chilled food distributors

Industry/Entity Type

Industry

Font styles to use
Sans Serif

Colors
0492cd
85cae6
cee9f5

Requirements
Must have
• Our logo
Nice to have
• Snow or ice background or image incorporated somehow

```html
<!DOCTYPE html>
<html lang="en">
<head>
<meta charset="utf-8">
<title>Frostvale Cold Packs – Business Cards</title>
<link rel="stylesheet" href="https://fonts.googleapis.com/css2?family=Arimo:wght@400;700&display=swap">
<style>
  :root {
    --backdrop: #25272d;
    --card-white: #ffffff;
    --brand-blue: #1a6fc4;
    --ice-deep: #4f8fd6;
    --ice-mid: #85b8e8;
    --ice-light: #cee9f5;
    --text-grey: #555a60;
    --wordmark-grey: #7d8288;
  }
  * { box-sizing: border-box; margin: 0; padding: 0; }
  html, body { width: 1200px; height: 900px; overflow: hidden; }
  body {
    background: var(--backdrop);
    font-family: "Arimo", Arial, sans-serif;
    position: relative;
  }
  .card {
    position: absolute;
    width: 665px;
    height: 380px;
    background: var(--card-white);
    display: flex;
    overflow: hidden;
    box-shadow: 0 14px 30px rgba(0,0,0,0.45);
  }
  .card--front { left: 268px; top: 40px; }
  .card--back  { left: 268px; top: 480px; }

  .ice-panel {
    height: 100%;
    background:
      radial-gradient(ellipse at 30% 35%, rgba(255,255,255,0.45), transparent 55%),
      radial-gradient(ellipse at 75% 70%, rgba(206,233,245,0.5), transparent 60%),
      linear-gradient(135deg, var(--ice-mid) 0%, var(--ice-deep) 55%, var(--ice-mid) 100%);
  }
  .card--front .ice-panel { width: 46%; border-right: 3px solid var(--brand-blue); }
  .card--back .ice-panel  { width: 44%; border-left: 3px solid var(--brand-blue); }

  .info-panel { flex: 1; position: relative; }

  /* Front */
  .brand {
    position: absolute; left: 38px; top: 52px;
    display: flex; align-items: center; gap: 14px;
  }
  .brand-dot { width: 30px; height: 30px; border-radius: 50%; background: var(--brand-blue); }
  .brand-name { font-size: 40px; font-weight: 700; color: var(--wordmark-grey); letter-spacing: 0.5px; }
  .tagline { font-size: 13px; color: var(--brand-blue); }
  .card--front .tagline { position: absolute; left: 82px; top: 98px; }

  .person { position: absolute; left: 82px; top: 148px; }
  .person-name { font-size: 26px; font-weight: 700; color: var(--brand-blue); }
  .person-role { font-size: 16px; color: var(--text-grey); margin-top: 2px; }

  .contact { position: absolute; left: 82px; bottom: 52px; font-size: 15px; color: var(--text-grey); line-height: 1.55; }

  /* Back */
  .card--back .info-panel { text-align: center; }
  .card--back .brand-name { display: block; font-size: 54px; margin-top: 46px; }
  .card--back .tagline { font-size: 16px; margin-top: 4px; }
  .office { margin-top: 28px; }
  .office + .office { margin-top: 22px; }
  .office-city { font-size: 18px; font-weight: 700; color: var(--brand-blue); letter-spacing: 0.5px; }
  .office-address { font-size: 17px; color: var(--text-grey); line-height: 1.35; margin-top: 6px; }
</style>
</head>
<body>

  <section class="card card--front" aria-label="Business card front">
    <div class="ice-panel" role="img" aria-label="Cracked blue ice texture"></div>
    <div class="info-panel">
      <div class="brand">
        <span class="brand-dot"></span>
        <span class="brand-name">Frostvale</span>
      </div>
      <p class="tagline">Keep your products chilled for longer</p>
      <div class="person">
        <p class="person-name">Dana Whitlock</p>
        <p class="person-role">Business Development</p>
      </div>
      <div class="contact">
        <p>dana.whitlock@frostvale.com.au</p>
        <p>www.frostvale.com.au</p>
      </div>
    </div>
  </section>

  <section class="card card--back" aria-label="Business card back">
    <div class="info-panel">
      <span class="brand-name">Frostvale</span>
      <p class="tagline">Keep your products chilled for longer</p>
      <div class="office">
        <p class="office-city">SYDNEY</p>
        <p class="office-address">14 Harbour Lane,<br>Westbay, NSW 2061</p>
      </div>
      <div class="office">
        <p class="office-city">AUCKLAND</p>
        <p class="office-address">21 Kauri Road, Greenhithe<br>Auckland 0632</p>
      </div>
    </div>
    <div class="ice-panel" role="img" aria-label="Cracked blue ice texture"></div>
  </section>

</body>
</html>
```